Poster Title Design

Create a text design concept for a documentary film called:
"The Orchard Beekeepers"
Background should be black, design elements and text should be red and/or white.
Design should be bold and readable from a distance.
Please provide at least 3 alternative concepts per submission.
(No need to include images or illustrations in the design. We only need a text treatment with optional simple graphic lines curves or blocks. There are no existing show logos.)
Please submit concepts centered in frame, 1200 wide x 1000 high jpg.
Thanks!
Good Luck!
- please use solid read and white colors for text and design elements.
- please do not use any fonts in the courier family.
please do not use any script or shadow fonts.
please do not use any other colors than red, white and black.
please avoid using gradients.
no need to include images or illustrations, just need the title text treatment.

```html
<!DOCTYPE html>
<html lang="en">
<head>
<meta charset="utf-8">
<title>The Orchard Beekeepers — Title Treatment</title>
<link rel="stylesheet" href="https://fonts.googleapis.com/css2?family=Archivo+Black&display=swap">
<style>
  :root {
    --ground: #000000;
    --type: #ffffff;
    --accent: #d80a0a;
  }

  html, body {
    margin: 0;
    padding: 0;
    width: 1200px;
    height: 675px;
    overflow: hidden;
    background: var(--ground);
  }

  .poster {
    position: relative;
    width: 1200px;
    height: 675px;
    background: var(--ground);
    overflow: hidden;
  }

  .coil-band {
    position: absolute;
    left: 0;
    top: 0;
    width: 1200px;
    height: 675px;
  }

  .coil-band__shape {
    fill: var(--accent);
  }

  .title {
    position: absolute;
    left: 0;
    top: 0;
    width: 1200px;
    height: 675px;
    margin: 0;
    font-family: "Archivo Black", "Arial Black", sans-serif;
    font-weight: 400;
    color: var(--type);
    text-align: center;
    text-transform: none;
  }

  .title__line {
    position: absolute;
    left: 0;
    width: 1200px;
    display: block;
    font-size: 140px;
    line-height: 1;
    letter-spacing: 0;
    white-space: nowrap;
  }

  .title__line--the { top: 104px; }
  .title__line--orchard { top: 289px; }
  .title__line--beekeepers { top: 477px; }
</style>
</head>
<body>
  <main class="poster">
    <svg class="coil-band" viewBox="0 0 1200 675" role="img"
         aria-label="Coil of barbed wire running diagonally from the upper left toward the lower right">
      <path class="coil-band__shape"
            d="M0 150 C 200 170, 400 260, 570 350 C 700 420, 790 520, 840 675 L 700 675 C 640 580, 520 500, 380 450 C 240 400, 100 370, 0 355 Z"/>
    </svg>

    <h1 class="title">
      <span class="title__line title__line--the">The</span>
      <span class="title__line title__line--orchard">Orchard</span>
      <span class="title__line title__line--beekeepers">Beekeepers</span>
    </h1>
  </main>
</body>
</html>
```